Women's Jewellery startup needs a captivating, beautifully designed and intuitive online store

[12/24 update]

Added 2 additional documents:

Feedback on designs received so far: designer feedback.docx
Product images from catalogue: products images.docx

Please read the feedback provided on designs provided so far to guide you further on your submission. The product images can be used to create promotional banners for the site.

@@@Added a document (VELISTO JEWELLERY_checklist.docx) which can be used by designers as a checklist when submitting their designs to ensure all aspects of the requirements have been covered @@@

+++IMPORTANT BUT NOT SPECIFIED IN THE REQUIREMENTS DOCUMENT - DESIGN SHOULD INCLUDE SUPPORT FOR MOBILE FRIENDLY SITE TOO+++

***Previous experience designing Jewellery online stores preferred (not essential)***

The name of the online Jewellery store is "Velisto Jewellery" and the business is based in Hong Kong. It will be run by 2 stay at home mothers. We need a Shopify themed store designed that will achieve the following objectives in order of priority:

• Conversion: The primary objective of the design/content is to prompt the customer to make a purchase. While this may sound obvious, it is mentioned so as not to distract the design process by focusing on other objectives (which are also important). The site also needs to be optimized so as to rank high in search engine searches for relevant keywords (SEO)
• Navigation: An intuitive interface which takes away a lot of the thinking from the customer by making it obvious what they need to do when they visit the store
• Engagement: Encourages the customer to spend time on the website and share content with their social network

Where applicable, the design of the store should reflect as closely as possible the mission statements and words outlined below:

• Jewellery you’ll fall in love with
• We want every client to leave the store with a smile
• We want to be able to provide the best service we can in every situation no matter what
• We aim to increase our business by word of mouth; therefore we tell people things about our store that makes it interesting for them to share
• We love every customer, no matter how difficult things get
• We, as a team, are so well informed about our products and brands that we always have the best information for our customers
• We celebrate women here!
• We celebrate life in here!
• We celebrate beauty here!
• We celebrate families here, as jewellery often stays within families.
• We will always try to make an extra step
• We will always try to exceed the expectation of our customers
• We will go as far as we possibly can to attract a customer back to our store and connect with us
• Every client that leaves our store knows more about jewellery because we passionately told him about it
• Romantic, classic, love, warm, cool, stylish

A draft functional specification is attached with this brief. We would like the design to reflect as closely as possible the functional requirements outlined in the document. Open to suggestions to improve upon the functional requirements.

Low design quality

Target Market(s)

Women aged 18-55

Industry/Entity Type

Jewelry Store

Coding

Coded - Design and coding required

Number of Pages Required

5+ page

Font styles to use
Other font styles liked:
• Myriad Pro as per Logo but open to any font that complements this one

Requirements
Must have
• 1. A look that encourages the user to make a purchase
• 2. An intuitive, easy to navigate and engaging interface
• 3. Primary colour scheme as defined in the functional specification attached
• 4. Simplistic look, not too cluttered
Nice to have
• 1. Closely matching the functional requirements of the site as outlined in the requirements specification but open to any better ideas

```html
<!DOCTYPE html>
<html lang="en">
<head>
<meta charset="utf-8">
<title>Velisto Jewellery</title>
<link href="https://fonts.googleapis.com/css2?family=Lato:wght@300;400;700;900&family=Poiret+One&family=Cinzel:wght@400;700&display=swap" rel="stylesheet">
<style>
:root{
  --gold:#9a7836;
  --ink:#222222;
  --text:#555555;
  --muted:#999999;
  --line:#e3e3e3;
  --soft:#f4f4f4;
  --card:#ffffff;
  --star:#f2b705;
  --dark:#2b2b2b;
}
*{margin:0;padding:0;box-sizing:border-box}
html,body{width:1200px;height:3513px;overflow:hidden}
body{position:relative;font-family:'Lato',sans-serif;color:var(--text);background:#fff}
.abs{position:absolute}

/* hero */
.hero{left:0;top:0;width:1200px;height:558px;background:radial-gradient(ellipse at 78% 45%,#e9c8bd 0%,#efe1dc 30%,#f1efee 60%,#f3f3f3 100%)}
.topbar{left:0;top:0;width:1200px;height:28px;font-size:10px;letter-spacing:.5px;color:#444}
.topbar .phone{left:164px;top:9px}
.topbar .links{left:714px;top:9px;display:flex;gap:28px}
.topbar .social{left:1012px;top:8px;display:flex;gap:16px}
.topbar .social span{width:10px;height:10px;border-radius:50%;background:#555;display:block}
.brand{left:196px;top:64px;width:140px;text-align:center}
.brand .mark{width:40px;height:40px;border-radius:50%;background:var(--ink);margin:0 auto 10px}
.brand .name{font-family:'Cinzel',serif;font-weight:700;font-size:17px;letter-spacing:3px;color:var(--ink)}
.nav{left:450px;top:56px;display:flex;gap:22px;font-size:11px;color:#333;letter-spacing:.5px}
.nav .cart{margin-left:14px;display:flex;gap:18px;align-items:center}
.hero-title{left:0;width:1200px;text-align:center;font-family:'Poiret One',sans-serif;color:#333}
.hero-sub{top:164px;font-size:38px;letter-spacing:2px}
.hero-main{top:212px;font-size:86px;letter-spacing:4px}
.hero-rule{left:258px;width:666px;height:1px;background:#555}
.hero-tag{left:0;top:324px;width:1200px;text-align:center;font-size:12px;letter-spacing:.6px;color:#333}
.btn-dark{left:520px;top:375px;width:140px;height:40px;background:var(--dark);color:#fff;font-size:11px;font-weight:700;letter-spacing:.5px;display:flex;align-items:center;justify-content:center}

/* headings */
.sec-title{left:0;width:1200px;text-align:center;font-size:16px;font-weight:700;color:var(--ink);letter-spacing:1px}
.sec-stars{left:0;width:1200px;display:flex;justify-content:center;align-items:center;gap:8px;color:var(--ink);font-size:10px}
.sec-stars i{display:block;width:34px;height:1px;background:#bbb}

/* collections */
.collection{top:684px;width:232px;height:232px;background:var(--soft);text-align:center}
.collection .pic{position:absolute;left:56px;top:10px;width:120px;height:140px;background:radial-gradient(circle,#e1e1e1 0%,#f4f4f4 70%)}
.collection h3{position:absolute;top:166px;width:100%;font-family:'Cinzel',serif;font-weight:400;font-size:22px;color:#333;letter-spacing:1px}
.collection p{position:absolute;top:204px;width:100%;font-size:12px;color:var(--gold)}

/* product grids */
.band{left:0;width:1200px;background:var(--soft)}
.card{background:var(--card)}
.card .pic{position:absolute;left:0;top:0;width:100%;background:radial-gradient(circle at 50% 50%,#dcdcdc 0%,#f1f1f1 45%,#fff 75%)}
.card .badge{position:absolute;left:16px;top:16px;width:46px;height:46px;border-radius:50%;background:var(--gold);color:#fff;font-size:12px;font-weight:700;display:flex;align-items:center;justify-content:center}
.card .badge.sale{left:auto;right:16px}
.card .name{position:absolute;left:18px;font-size:12px;color:#333;line-height:17px}
.card .price{position:absolute;right:18px;text-align:right;font-size:15px;font-weight:700;color:var(--ink);line-height:20px}
.card .price s{display:block;font-weight:400;font-size:14px;color:var(--muted)}
.card .rate{position:absolute;left:18px;font-size:11px;color:var(--star);letter-spacing:1px}
.card .rate .off{color:#ccc}
.card.hover{box-shadow:0 4px 14px rgba(0,0,0,.18)}
.card .tools{position:absolute;left:0;width:100%;height:30px;border-top:1px solid var(--line);border-bottom:1px solid var(--line);display:flex;background:#fff}
.card .tools span{flex:1;display:flex;align-items:center;justify-content:center;border-right:1px solid var(--line)}
.card .tools span:last-child{border-right:0}

/* banner */
.banner{left:0;top:1933px;width:1200px;height:509px;background:linear-gradient(100deg,#8a7570 0%,#b9a5a1 35%,#6e4a47 65%,#3d2623 100%)}
.banner-copy{left:0;top:2250px;width:1200px;text-align:center;font-size:11px;color:#fff;line-height:17px}
.banner-link{left:0;top:2298px;width:1200px;text-align:center;font-size:10px;color:#e9d3a2}

.arrow{width:18px;height:18px;border-radius:50%;background:#e2e2e2;display:flex;align-items:center;justify-content:center}

/* newsletter */
.news-copy{left:0;top:3078px;width:1200px;text-align:center;font-size:12px;color:#555}
.news-input{left:398px;top:3113px;width:495px;height:38px;border:1px solid #ddd;font-size:11px;color:#aaa;padding:12px 14px}
.news-btn{left:893px;top:3113px;width:40px;height:38px;background:var(--gold);display:flex;align-items:center;justify-content:center}

/* footer */
.rule{left:0;width:1200px;height:1px;background:var(--line)}
.foot-col h4{font-size:12px;font-weight:700;color:var(--ink);letter-spacing:.5px;margin-bottom:16px}
.foot-col li{list-style:none;font-size:12px;color:#444;line-height:28px}
.bottombar{left:0;top:3441px;width:1200px;height:72px;background:var(--dark)}
.bottombar .mark{position:absolute;left:166px;top:22px;width:26px;height:26px;border-radius:50%;background:#ddd}
.bottombar .copy{position:absolute;left:204px;top:30px;font-size:10px;color:#bbb;letter-spacing:.3px}
</style>
</head>
<body>

<!-- HERO -->
<div class="abs hero" role="img" aria-label="Photograph of a woman's hand wearing ornate rose gold rings"></div>
<div class="abs topbar">
  <div class="abs phone">PHONE SHOPPING: 1-800-555-0142</div>
  <div class="abs links"><span>SIGN IN</span><span>WISHLIST</span><span>ENGLISH ▾</span><span>USD $ ▾</span></div>
  <div class="abs social"><span></span><span></span><span></span></div>
</div>
<div class="abs brand"><div class="mark"></div><div class="name">VELISTO</div></div>
<nav class="abs nav">
  <span>HOME</span><span>CATEGORIES ▾</span><span>PRODUCT ▾</span><span>COMBINATION ▾</span><span>PAGES ▾</span><span>BLOG</span>
  <span class="cart">
    <svg width="12" height="12" viewBox="0 0 12 12"><circle cx="5" cy="5" r="3.8" fill="none" stroke="#333" stroke-width="1.4"/><line x1="8" y1="8" x2="11.3" y2="11.3" stroke="#333" stroke-width="1.4"/></svg>
    <span>CART (0)</span>
  </span>
</nav>
<div class="abs hero-title hero-sub">Live The Moment</div>
<div class="abs hero-title hero-main">World Jewelry</div>
<div class="abs hero-rule" style="top:316px"></div>
<div class="abs hero-tag">WHEN YOU HAVE CONFIDENCE, YOU CAN HAVE A LOT OF FUN. AND WHEN YOU HAVE FUN, YOU CAN DO AMAZING THINGS</div>
<div class="abs hero-rule" style="top:344px"></div>
<div class="abs btn-dark">SEE COLLECTIONS</div>

<!-- POPULAR COLLECTIONS -->
<div class="abs sec-title" style="top:614px">POPULAR COLLECTIONS</div>
<div class="abs sec-stars" style="top:642px"><i></i>★★★<i></i></div>
<div class="abs collection" style="left:94px"><div class="pic" role="img" aria-label="Diamond solitaire ring"></div><h3>RINGS</h3><p>See the Collection</p></div>
<div class="abs collection" style="left:352px"><div class="pic" role="img" aria-label="Pair of diamond drop earrings"></div><h3>EARRINGS</h3><p>See the Collection</p></div>
<div class="abs collection" style="left:609px"><div class="pic" role="img" aria-label="Diamond pendant necklace"></div><h3>NECKLACES</h3><p>See the Collection</p></div>
<div class="abs collection" style="left:867px"><div class="pic" role="img" aria-label="Silver flower bracelet"></div><h3>BRACELETS</h3><p>See the Collection</p></div>

<!-- NEW PRODUCTS -->
<div class="abs band" style="top:961px;height:972px"></div>
<div class="abs sec-title" style="top:988px">NEW PRODUCTS</div>
<div class="abs sec-stars" style="top:1015px"><i></i>★★★<i></i></div>

<div class="abs card" style="left:141px;top:1052px;width:293px;height:385px">
  <div class="pic" style="height:272px" role="img" aria-label="Pink heart diamond ring"></div>
  <div class="badge">New</div>
  <div class="name" style="top:312px">Premium Green Coat</div>
  <div class="price" style="top:310px">$40.00</div>
  <div class="rate" style="top:336px">★★★★★</div>
</div>
<div class="abs card hover" style="left:457px;top:1052px;width:293px;height:398px">
  <div class="pic" style="height:256px" role="img" aria-label="Silver swirl diamond pendant"></div>
  <div class="badge">New</div>
  <div class="tools" style="top:256px">
    <span><svg width="13" height="13" viewBox="0 0 12 12"><circle cx="5" cy="5" r="3.8" fill="none" stroke="#333" stroke-width="1.4"/><line x1="8" y1="8" x2="11.3" y2="11.3" stroke="#333" stroke-width="1.4"/></svg></span>
    <span><svg width="13" height="12" viewBox="0 0 13 12"><g fill="#333"><rect x="0" y="1" width="2" height="2"/><rect x="0" y="5" width="2" height="2"/><rect x="0" y="9" width="2" height="2"/><rect x="4" y="1.5" width="9" height="1"/><rect x="4" y="5.5" width="9" height="1"/><rect x="4" y="9.5" width="9" height="1"/></g></svg></span>
    <span><svg width="13" height="12" viewBox="0 0 24 22"><path d="M12 21 2.5 11.5A5.5 5.5 0 0 1 12 4a5.5 5.5 0 0 1 9.5 7.5Z" fill="#222"/></svg></span>
    <span><svg width="13" height="12" viewBox="0 0 13 12"><path d="M1 4h10M8 1l3 3-3 3M12 8H2M5 5 2 8l3 3" fill="none" stroke="#333" stroke-width="1.3"/></svg></span>
  </div>
  <div class="name" style="top:308px">Maximus Quam<br>Posuere</div>
  <div class="price" style="top:308px">$100.00</div>
  <div class="rate" style="top:350px">★★★★★</div>
</div>
<div class="abs card" style="left:776px;top:1052px;width:293px;height:385px">
  <div class="pic" style="height:272px" role="img" aria-label="Halo diamond engagement ring"></div>
  <div class="badge">New</div><div class="badge sale">Sale</div>
  <div class="name" style="top:312px">Printed Summer Dress</div>
  <div class="price" style="top:310px">$150.00</div>
  <div class="rate" style="top:336px">★★★★★</div>
</div>

<div class="abs card" style="left:141px;top:1502px;width:293px;height:389px">
  <div class="pic" style="height:282px" role="img" aria-label="Bow shaped diamond hoop earrings"></div>
  <div class="badge">New</div>
  <div class="name" style="top:310px">Printed Chiffon Dress</div>
  <div class="price" style="top:300px"><s>$20.50</s>$16.40</div>
  <div class="rate" style="top:336px">★★★★★</div>
</div>
<div class="abs card" style="left:457px;top:1502px;width:293px;height:389px">
  <div class="pic" style="height:282px" role="img" aria-label="Diamond solitaire engagement ring"></div>
  <div class="badge">New</div>
  <div class="name" style="top:310px">Printed Summer Dress</div>
  <div class="price" style="top:308px">$30.50</div>
  <div class="rate" style="top:336px">★★★★<span class="off">★</span></div>
</div>
<div class="abs card" style="left:776px;top:1502px;width:293px;height:389px">
  <div class="pic" style="height:282px" role="img" aria-label="Pair of diamond cluster stud earrings"></div>
  <div class="badge">New</div>
  <div class="name" style="top:310px">Maximus Quam<br>Posuere</div>
  <div class="price" style="top:300px"><s>$30.50</s>$28.98</div>
  <div class="rate" style="top:350px">★★★★★</div>
</div>

<!-- BANNER -->
<div class="abs banner" role="img" aria-label="Close-up photograph of two diamond wedding bands"></div>
<div class="abs banner-copy">Sed do eiusmod tempor incididunt ut labore et dolore magna aliqua.<br>Ut enim ad minim veniam, quis nostrud exercitation ullamco laboris nisi ut aliquip ex ea commodo consequat.</div>
<div class="abs banner-link">Shop Now</div>

<!-- OUR PRODUCTS -->
<div class="abs band" style="top:2496px;height:452px"></div>
<div class="abs sec-title" style="top:2518px">OUR PRODUCTS</div>
<div class="abs sec-stars" style="top:2545px"><i></i>★★★<i></i></div>
<div class="abs arrow" style="left:143px;top:2710px"><svg width="6" height="9" viewBox="0 0 6 9"><path d="M5 1 1 4.5 5 8" fill="none" stroke="#888" stroke-width="1.4"/></svg></div>
<div class="abs arrow" style="left:1000px;top:2710px"><svg width="6" height="9" viewBox="0 0 6 9"><path d="M1 1l4 3.5L1 8" fill="none" stroke="#888" stroke-width="1.4"/></svg></div>

<div class="abs card" style="left:152px;top:2580px;width:192px;height:291px">
  <div class="pic" style="height:190px" role="img" aria-label="Pink heart diamond ring"></div>
  <div class="badge" style="width:40px;height:40px;left:12px;top:12px">New</div>
  <div class="name" style="top:208px;left:14px">Curabitur<br>Cursus Dignis</div>
  <div class="price" style="top:206px;right:14px">$90.00</div>
  <div class="rate" style="top:250px;left:14px">★★★★★</div>
</div>
<div class="abs card hover" style="left:375px;top:2580px;width:194px;height:288px">
  <div class="pic" style="height:160px" role="img" aria-label="Pink heart diamond ring"></div>
  <div class="badge" style="width:40px;height:40px;left:12px;top:12px">New</div>
  <div class="tools" style="top:160px;height:28px">
    <span><svg width="12" height="12" viewBox="0 0 12 12"><circle cx="5" cy="5" r="3.8" fill="none" stroke="#333" stroke-width="1.4"/><line x1="8" y1="8" x2="11.3" y2="11.3" stroke="#333" stroke-width="1.4"/></svg></span>
    <span><svg width="12" height="11" viewBox="0 0 13 12"><g fill="#333"><rect x="0" y="1" width="2" height="2"/><rect x="0" y="5" width="2" height="2"/><rect x="0" y="9" width="2" height="2"/><rect x="4" y="1.5" width="9" height="1"/><rect x="4" y="5.5" width="9" height="1"/><rect x="4" y="9.5" width="9" height="1"/></g></svg></span>
    <span><svg width="12" height="11" viewBox="0 0 24 22"><path d="M12 21 2.5 11.5A5.5 5.5 0 0 1 12 4a5.5 5.5 0 0 1 9.5 7.5Z" fill="#222"/></svg></span>
    <span><svg width="12" height="11" viewBox="0 0 13 12"><path d="M1 4h10M8 1l3 3-3 3M12 8H2M5 5 2 8l3 3" fill="none" stroke="#333" stroke-width="1.3"/></svg></span>
  </div>
  <div class="name" style="top:206px;left:14px">Printed<br>Summer Dress</div>
  <div class="price" style="top:204px;right:14px">$26.99</div>
  <div class="rate" style="top:248px;left:14px">★★★★★</div>
</div>
<div class="abs card" style="left:598px;top:2580px;width:192px;height:291px">
  <div class="pic" style="height:190px" role="img" aria-label="Diamond ball pendant necklace"></div>
  <div class="badge" style="width:40px;height:40px;left:12px;top:12px">New</div>
  <div class="name" style="top:208px;left:14px">Curabitur<br>Cursus Dignis</div>
  <div class="price" style="top:206px;right:14px">$50.99</div>
  <div class="rate" style="top:250px;left:14px"><span class="off">★★★★★</span></div>
</div>
<div class="abs card" style="left:820px;top:2580px;width:192px;height:291px">
  <div class="pic" style="height:190px" role="img" aria-label="Pair of diamond cluster stud earrings"></div>
  <div class="badge" style="width:40px;height:40px;left:12px;top:12px">New</div>
  <div class="name" style="top:208px;left:14px">Maximus Quam<br>Posuere</div>
  <div class="price" style="top:198px;right:14px"><s>$30.50</s>$28.98</div>
  <div class="rate" style="top:250px;left:14px">★★★★★</div>
</div>
<div class="abs rule" style="top:2930px;left:140px;width:880px;background:#ddd"></div>

<!-- NEWSLETTER -->
<div class="abs sec-title" style="top:2994px">NEWSLETTER</div>
<div class="abs sec-stars" style="top:3021px"><i></i>★★★<i></i></div>
<div class="abs news-copy">You may unsubscribe at any moment. For that purpose, please find our contact info in the legal notice.</div>
<div class="abs news-input">Your e-mail</div>
<div class="abs news-btn"><svg width="16" height="16" viewBox="0 0 16 16"><path d="M15 1 1 7l5 2 2 5Z M15 1 6 9" fill="#fff" stroke="#fff" stroke-width="1" stroke-linejoin="round"/></svg></div>

<!-- FOOTER -->
<div class="abs rule" style="top:3216px"></div>
<div class="abs foot-col" style="left:171px;top:3262px"><h4>SUPPORT CUSTOMER</h4><ul><li>Preferences</li><li>Order History</li><li>Wish List</li><li>Sign In</li></ul></div>
<div class="abs foot-col" style="left:424px;top:3262px"><h4>CUSTOMER</h4><ul><li>Return Policy</li><li>Privacy Policy</li><li>Help &amp; Contact</li><li>Shipper</li></ul></div>
<div class="abs foot-col" style="left:680px;top:3262px"><h4>ABOUT US</h4><ul><li>Store Locations</li><li>Whosesalers</li><li>Map Site</li><li>Contact Us</li></ul></div>
<div class="abs foot-col" style="left:930px;top:3262px"><h4>INFORMATION</h4><ul><li>FAQ</li><li>Advance Search</li><li>Gift Cards</li><li>Shop By Brands</li></ul></div>
<div class="abs bottombar"><div class="mark"></div><div class="copy">© 2017 VELISTO  -  All rights reserved</div></div>

</body>
</html>
```